Small boutique multi-family apartment developer needs premium website design.

We are a growing real estate development company specializing in multi family apartment development. Our company Mireval Stone Development focuses on passive real estate investors looking to maximize their current real estate portfolio by allowing us to develop and reposition their current properties allowing them more cashflow while we are also able to take over the management of their asset in order to ensure optimal performance on a consistent basis.

```html
<!DOCTYPE html>
<html lang="en">
<head>
<meta charset="utf-8">
<title>Mireval Stone Development</title>
<link href="https://fonts.googleapis.com/css2?family=Outfit:wght@300;400;500;600;700&family=Inter:wght@400;500;600&display=swap" rel="stylesheet">
<style>
:root{
  --red:#a51d24;
  --red-dark:#8e171d;
  --ink:#222326;
  --muted:#8a8a8a;
  --line:#d9d9d9;
  --soft:#f6f6f6;
  --page:#fdfbfb;
  --footer:#2e2e2f;
  --white:#ffffff;
  --gold:#f2c200;
}
*{box-sizing:border-box;margin:0;padding:0}
html,body{width:1200px;height:4545px;overflow:hidden}
body{position:relative;background:var(--page);font-family:"Outfit",sans-serif;color:var(--ink)}
.abs{position:absolute}
.body-text{font-family:"Inter",sans-serif}

/* nav */
.site-nav{position:absolute;left:0;top:0;width:1200px;height:99px;background:var(--white)}
.brand{position:absolute;left:97px;top:25px;display:flex;align-items:center;gap:14px;height:49px}
.brand-square{width:44px;height:44px;border:5px solid var(--red)}
.brand-name{font-size:14px;color:var(--red);font-weight:500}
.nav-links{position:absolute;top:38px;left:826px;display:flex;gap:0}
.nav-links a{position:absolute;font-size:15px;color:var(--muted);text-decoration:none;white-space:nowrap}
.nav-links a.active{color:var(--red)}

/* hero */
.hero{position:absolute;left:0;top:99px;width:1200px;height:542px;background:linear-gradient(180deg,#4d4150 0%,#5d4a4c 40%,#3a3532 75%,#5a5652 100%)}
.hero-title{position:absolute;left:0;top:150px;width:1200px;text-align:center;color:var(--white);font-weight:600;font-size:50px;line-height:74px}
.hero-sub{position:absolute;left:0;top:315px;width:1200px;text-align:center;color:var(--white);font-size:31px;font-weight:400}
.search{position:absolute;left:348px;top:397px;width:503px;height:46px;background:var(--white);border-radius:23px;overflow:hidden}
.search span{position:absolute;left:26px;top:13px;font-size:16px;color:#9a9a9a}
.search-btn{position:absolute;right:0;top:0;width:67px;height:46px;background:var(--red);border-radius:0 23px 23px 0;display:flex;align-items:center;justify-content:center}

.eyebrow{position:absolute;font-size:15px;color:var(--red)}
.section-title{position:absolute;font-size:32px;font-weight:500;line-height:41px;color:var(--ink)}

/* about cards */
.about-text{position:absolute;left:752px;top:733px;width:350px;font-size:14.5px;line-height:22.5px;color:#444}
.about-card{position:absolute;top:890px;width:307px}
.about-card .photo{height:176px}
.about-card h3{margin-top:14px;font-size:29px;font-weight:400;color:#6b6b6b}
.about-card .more{margin-top:10px;display:flex;justify-content:space-between;align-items:center;font-size:15px;color:var(--red)}

/* expertise */
.service{position:absolute;left:97px;width:450px;border-radius:20px;background:var(--soft);padding:26px 26px}
.service h4{font-size:18px;font-weight:500;color:var(--ink)}
.service p{margin-top:8px;font-size:14px;color:#999}
.service.featured{background:var(--white);box-shadow:0 4px 18px rgba(0,0,0,.07);border:1px solid #eee}
.service.featured h4{color:var(--red)}

/* properties */
.select{position:absolute;top:2097px;height:49px;border:1px solid #888;border-radius:3px;background:var(--white);font-size:20px;padding:12px 14px;display:flex;align-items:center;justify-content:space-between}
.filter-btn{position:absolute;left:469px;top:2097px;width:131px;height:49px;background:var(--red);color:var(--white);border-radius:3px;font-size:20px;display:flex;align-items:center;justify-content:center}
.property{position:absolute;top:2187px;width:316px;height:665px;border:2px solid #c9c9c9;border-radius:4px;background:var(--white);overflow:hidden}
.property .photo{position:absolute;left:0;top:0;width:312px;height:362px}
.badge{position:absolute;left:0;top:357px;height:20px;padding:0 8px;background:var(--gold);color:#333;font-size:9.5px;display:flex;align-items:center;gap:3px;font-family:"Inter",sans-serif}
.price{position:absolute;left:29px;top:392px;font-size:22px;font-weight:600;color:var(--red)}
.fav{position:absolute;left:182px;top:393px;width:32px;height:32px;border-radius:50%;background:var(--white);box-shadow:0 1px 6px rgba(0,0,0,.18);display:flex;align-items:center;justify-content:center}
.ptype{position:absolute;left:29px;top:425px;font-size:22px;font-weight:500}
.addr{position:absolute;left:29px;top:460px;font-size:13px;color:#777}
.feats{position:absolute;left:29px;top:506px;display:flex;gap:12px;font-size:11.5px;color:#555;font-family:"Inter",sans-serif}
.feats span{display:flex;align-items:center;gap:5px}
.btn-primary,.btn-ghost{position:absolute;left:29px;width:254px;height:41px;border-radius:4px;display:flex;align-items:center;justify-content:center;font-size:14px}
.btn-primary{top:557px;border:1.5px solid var(--red);color:var(--red)}
.btn-ghost{top:609px;border:1.5px solid #aaa;color:#999}
.page-box{position:absolute;top:2900px;width:25px;height:25px;display:flex;align-items:center;justify-content:center;font-size:13px;background:#e9e5e5;color:#777}
.page-box.current{background:var(--red);color:var(--white)}

/* contact */
.form-card{position:absolute;left:717px;top:3032px;width:384px;height:480px;background:var(--white);border-radius:8px;box-shadow:0 4px 24px rgba(0,0,0,.1)}
.field-label{position:absolute;left:28px;font-size:13px;color:#333;font-family:"Inter",sans-serif}
.field{position:absolute;left:28px;width:330px;height:42px;border:1px solid #e6e6e6;border-radius:4px;padding:13px 14px;font-size:12px;color:#777;font-family:"Inter",sans-serif}
.submit{position:absolute;left:28px;top:408px;width:330px;height:51px;background:var(--red);border-radius:6px;color:var(--white);font-size:14px;font-weight:600;display:flex;align-items:center;justify-content:center}

/* testimonials */
.center{position:absolute;left:0;width:1200px;text-align:center}
.testi{position:absolute;top:3791px;width:271px;height:201px;border:1px solid #e4e4e4;background:var(--white);padding:28px 28px}
.stars{display:flex;gap:5px}
.testi p{margin-top:16px;font-size:11.5px;line-height:20px;color:#888;font-family:"Inter",sans-serif}
.person{margin-top:12px;display:flex;align-items:center;gap:12px}
.avatar{width:38px;height:38px;border-radius:50%;background:linear-gradient(135deg,#b9a79a,#6f625b)}
.person b{display:block;font-weight:400;font-size:11px;color:var(--red)}
.person i{display:block;font-style:normal;font-size:11.5px;color:#444;margin-top:4px}
.nav-dot{position:absolute;top:3872px;width:40px;height:40px;border-radius:50%;background:#b9b9be;display:flex;align-items:center;justify-content:center}

/* footer */
.site-footer{position:absolute;left:0;top:4082px;width:1200px;height:463px;background:var(--footer);color:var(--white)}
.foot-brand{position:absolute;left:97px;top:27px;display:flex;align-items:center;gap:28px}
.foot-square{width:78px;height:78px;border:6px solid #e6e6e6}
.foot-brand span{font-size:26px;font-weight:400;color:#eee}
.foot-head{position:absolute;font-size:15px;font-weight:600;font-family:"Inter",sans-serif}
.foot-link{position:absolute;font-size:12.5px;color:#ddd;font-family:"Inter",sans-serif}
.social{position:absolute;top:76px;width:24px;height:24px;border-radius:50%;background:#f2f2f2}
.info{position:absolute;left:409px;display:flex;gap:12px;font-size:12.5px;color:#ddd;font-family:"Inter",sans-serif;line-height:15px}
</style>
</head>
<body>

<header class="site-nav">
  <div class="brand"><div class="brand-square"></div><span class="brand-name">Mireval Stone Development</span></div>
  <nav class="nav-links">
    <a class="active" style="left:0">Home</a>
    <a style="left:74px">About</a>
    <a style="left:148px">News</a>
    <a style="left:219px">Contact</a>
  </nav>
</header>

<section class="hero" role="img" aria-label="Modern two-storey house with lit garage at dusk">
  <h1 class="hero-title">Welcome to Mireval Stone<br>Development</h1>
  <p class="hero-sub">International Asset Development</p>
  <div class="search">
    <span>Enter address, city, zip, neighbourhood, or #MLS</span>
    <div class="search-btn"><svg width="22" height="22" viewBox="0 0 24 24" fill="none" stroke="#fff" stroke-width="2.2"><circle cx="11" cy="11" r="7"/><path d="M16 16l5 5"/></svg></div>
  </div>
</section>

<!-- about -->
<span class="eyebrow" style="left:97px;top:696px">About</span>
<h2 class="section-title" style="left:97px;top:722px;width:480px">Committed to the fundamentals of investing, to ensure longterm growth</h2>
<p class="about-text body-text">Lorem ipsum dolor sit amet, consectetur adipiscing elit. Nunc vulputate libero et velit interdum, ac aliquet odio mattis. Class aptent taciti sociosqu ad litora torquent per conubia nostra, per inceptos himenaeos. Curabitur</p>

<article class="about-card" style="left:97px">
  <div class="photo" role="img" aria-label="Team meeting around a table with sticky notes on the wall" style="background:linear-gradient(135deg,#d8d3cc,#8d7f74)"></div>
  <h3>Our Culture &amp; Values</h3>
  <div class="more">Read more<svg width="28" height="20" viewBox="0 0 28 20"><rect width="28" height="20" rx="10" fill="#a51d24"/><path d="M8 10h12M15 5l5 5-5 5" stroke="#fff" stroke-width="2" fill="none"/></svg></div>
</article>
<article class="about-card" style="left:447px">
  <div class="photo" role="img" aria-label="Modern home entrance with garden path at evening" style="background:linear-gradient(135deg,#8aa0b5,#4e5a4c)"></div>
  <h3>Our History</h3>
  <div class="more">Read more<svg width="28" height="20" viewBox="0 0 28 20"><rect width="28" height="20" rx="10" fill="#a51d24"/><path d="M8 10h12M15 5l5 5-5 5" stroke="#fff" stroke-width="2" fill="none"/></svg></div>
</article>
<article class="about-card" style="left:794px">
  <div class="photo" role="img" aria-label="Two business people shaking hands" style="background:linear-gradient(135deg,#c9a48f,#7f8fa6)"></div>
  <h3>Our Leadership</h3>
  <div class="more">Read more<svg width="28" height="20" viewBox="0 0 28 20"><rect width="28" height="20" rx="10" fill="#a51d24"/><path d="M8 10h12M15 5l5 5-5 5" stroke="#fff" stroke-width="2" fill="none"/></svg></div>
</article>

<!-- expertise -->
<span class="eyebrow" style="left:97px;top:1257px">Our Expertise</span>
<h2 class="section-title" style="left:97px;top:1284px;width:480px">Our success is a reflection of our experience</h2>

<div class="service featured" style="top:1405px;height:134px;padding:0">
  <svg class="abs" style="left:30px;top:30px" width="76" height="72" viewBox="0 0 76 72"><rect x="6" y="34" width="12" height="34" fill="#c96a6e"/><rect x="26" y="6" width="13" height="62" fill="#a51d24"/><rect x="46" y="26" width="12" height="42" fill="#c96a6e"/><rect x="0" y="64" width="76" height="5" fill="#d29a9c"/></svg>
  <h4 class="abs" style="left:136px;top:42px">Investments</h4>
  <p class="abs" style="left:136px;top:74px;margin:0">It has roots in a piece of classical</p>
</div>
<div class="service" style="top:1546px;height:99px"><h4>Development &amp; Construction</h4><p>Lorem Ipsum is not simply random text</p></div>
<div class="service" style="top:1652px;height:99px"><h4>Acquisitions</h4><p>Lorem Ipsum is not simply random text</p></div>
<div class="service" style="top:1758px;height:99px"><h4>Asset Management</h4><p>Lorem Ipsum is not simply random text</p></div>
<div class="abs" role="img" aria-label="White modern multi-family apartment building with black balconies and a palm tree" style="left:600px;top:1405px;width:600px;height:489px;background:linear-gradient(160deg,#3f86d6 0%,#8fbde9 45%,#e9ecee 70%,#8b8f86 100%)"></div>

<!-- properties -->
<h2 class="section-title" style="left:97px;top:1992px;font-size:32px">Current Offered Properties</h2>
<div class="abs" style="left:97px;top:2070px;width:1004px;height:2px;background:var(--line)"></div>
<div class="select" style="left:101px;width:173px">Select Type<svg width="16" height="10" viewBox="0 0 16 10"><path d="M2 2l6 6 6-6" stroke="#333" stroke-width="1.6" fill="none"/></svg></div>
<div class="select" style="left:284px;width:175px">Select Price<svg width="16" height="10" viewBox="0 0 16 10"><path d="M2 2l6 6 6-6" stroke="#333" stroke-width="1.6" fill="none"/></svg></div>
<div class="filter-btn">Set filters</div>

<article class="property" style="left:101px">
  <div class="photo" role="img" aria-label="Stucco family house with brown shutters and front lawn" style="background:linear-gradient(180deg,#b6d3ee 0%,#d9cfc2 45%,#c9bfb1 70%,#6f9a3d 100%)"></div>
  <div class="badge">✦ Available now</div>
  <div class="price">$700</div>
  <div class="fav"><svg width="14" height="13" viewBox="0 0 24 22"><path d="M12 20S2 13.5 2 7.5A5 5 0 0 1 12 5a5 5 0 0 1 10 2.5C22 13.5 12 20 12 20z" stroke="#a51d24" stroke-width="2.4" fill="none"/></svg></div>
  <div class="ptype">Type A01</div>
  <div class="addr body-text">2418 Cedar Ridge, Lakemont, FL</div>
  <div class="feats"><span><svg width="14" height="10" viewBox="0 0 14 10"><path d="M1 9V2M1 6h12v3M3 6V4h4v2" stroke="#a51d24" stroke-width="1.3" fill="none"/></svg>3 Rooms</span><span><svg width="14" height="10" viewBox="0 0 14 10"><path d="M1 4h12v2a3 3 0 0 1-3 3H4a3 3 0 0 1-3-3zM3 4V2h2" stroke="#a51d24" stroke-width="1.3" fill="none"/></svg>3 Bathrooms</span><span><svg width="12" height="12" viewBox="0 0 12 12"><path d="M1 11L6 2l5 9z" stroke="#333" stroke-width="1.2" fill="none"/></svg>12×5m²</span></div>
  <div class="btn-primary">Book Now</div>
  <div class="btn-ghost">More details</div>
</article>
<article class="property" style="left:443px">
  <div class="photo" role="img" aria-label="White cottage house with dark slate roof and gables" style="background:linear-gradient(180deg,#cfe2f5 0%,#7a818a 35%,#ecebe3 65%,#d8d6cf 100%)"></div>
  <div class="badge">✦ Available now</div>
  <div class="price">$700</div>
  <div class="fav"><svg width="14" height="13" viewBox="0 0 24 22"><path d="M12 20S2 13.5 2 7.5A5 5 0 0 1 12 5a5 5 0 0 1 10 2.5C22 13.5 12 20 12 20z" stroke="#a51d24" stroke-width="2.4" fill="none"/></svg></div>
  <div class="ptype">Type A01</div>
  <div class="addr body-text">2418 Cedar Ridge, Lakemont, FL</div>
  <div class="feats"><span><svg width="14" height="10" viewBox="0 0 14 10"><path d="M1 9V2M1 6h12v3M3 6V4h4v2" stroke="#a51d24" stroke-width="1.3" fill="none"/></svg>3 Rooms</span><span><svg width="14" height="10" viewBox="0 0 14 10"><path d="M1 4h12v2a3 3 0 0 1-3 3H4a3 3 0 0 1-3-3zM3 4V2h2" stroke="#a51d24" stroke-width="1.3" fill="none"/></svg>3 Bathrooms</span><span><svg width="12" height="12" viewBox="0 0 12 12"><path d="M1 11L6 2l5 9z" stroke="#333" stroke-width="1.2" fill="none"/></svg>12×5m²</span></div>
  <div class="btn-primary">Book Now</div>
  <div class="btn-ghost">More details</div>
</article>
<article class="property" style="left:785px">
  <div class="photo" role="img" aria-label="Brick suburban house with grey garage door and lawn" style="background:linear-gradient(180deg,#bcd8f1 0%,#6a6a70 35%,#9c8c80 60%,#5e8a3a 100%)"></div>
  <div class="badge">✦ Available now</div>
  <div class="price">$700</div>
  <div class="fav"><svg width="14" height="13" viewBox="0 0 24 22"><path d="M12 20S2 13.5 2 7.5A5 5 0 0 1 12 5a5 5 0 0 1 10 2.5C22 13.5 12 20 12 20z" stroke="#a51d24" stroke-width="2.4" fill="none"/></svg></div>
  <div class="ptype">Type A01</div>
  <div class="addr body-text">2418 Cedar Ridge, Lakemont, FL</div>
  <div class="feats"><span><svg width="14" height="10" viewBox="0 0 14 10"><path d="M1 9V2M1 6h12v3M3 6V4h4v2" stroke="#a51d24" stroke-width="1.3" fill="none"/></svg>3 Rooms</span><span><svg width="14" height="10" viewBox="0 0 14 10"><path d="M1 4h12v2a3 3 0 0 1-3 3H4a3 3 0 0 1-3-3zM3 4V2h2" stroke="#a51d24" stroke-width="1.3" fill="none"/></svg>3 Bathrooms</span><span><svg width="12" height="12" viewBox="0 0 12 12"><path d="M1 11L6 2l5 9z" stroke="#333" stroke-width="1.2" fill="none"/></svg>12×5m²</span></div>
  <div class="btn-primary">Book Now</div>
  <div class="btn-ghost">More details</div>
</article>

<svg class="abs" style="left:893px;top:2903px" width="12" height="18" viewBox="0 0 12 18"><path d="M11 1L1 9l10 8z" fill="#444"/></svg>
<div class="page-box current" style="left:922px">1</div>
<div class="page-box" style="left:960px">2</div>
<div class="page-box" style="left:998px">3</div>
<div class="page-box" style="left:1037px">4</div>
<svg class="abs" style="left:1080px;top:2903px" width="12" height="18" viewBox="0 0 12 18"><path d="M1 1l10 8-10 8z" fill="#444"/></svg>

<!-- contact -->
<span class="eyebrow" style="left:97px;top:3216px">Contact Us</span>
<h2 class="section-title" style="left:97px;top:3243px;width:520px">Get in Touch with Harborline Homes We're Here to Help</h2>
<form class="form-card">
  <label class="field-label" style="top:26px">Name</label>
  <div class="field" style="top:48px">Your name</div>
  <label class="field-label" style="top:107px">Email</label>
  <div class="field" style="top:129px">Email</div>
  <label class="field-label" style="top:188px">Phone</label>
  <div class="field" style="top:210px">phone number</div>
  <label class="field-label" style="top:278px">Message</label>
  <div class="field" style="top:300px;height:88px">Write message</div>
  <div class="submit">Submit</div>
</form>

<!-- testimonials -->
<p class="center" style="top:3635px;font-size:15px;color:var(--red)">Testimonials</p>
<h2 class="center" style="top:3660px;font-size:32px;font-weight:500">Hear from Our Satisfied Clients</h2>
<p class="center body-text" style="top:3711px;font-size:13px;line-height:18px;color:#c8c8c8">lorem ipsum dolor sit amet, consectetur adipiscing elit. Nunc vulputate libero et velit<br>interdum, ac aliquet odio mattis.</p>

<div class="nav-dot" style="left:81px"><svg width="12" height="16" viewBox="0 0 12 16"><path d="M9 2L3 8l6 6" stroke="#fff" stroke-width="2" fill="none"/></svg></div>
<div class="nav-dot" style="left:1078px"><svg width="12" height="16" viewBox="0 0 12 16"><path d="M3 2l6 6-6 6" stroke="#fff" stroke-width="2" fill="none"/></svg></div>

<article class="testi" style="left:164px">
  <div class="stars"><svg width="110" height="18" viewBox="0 0 110 18"><g fill="#f2c200"><path id="st" d="M9 1l2.4 5 5.4.7-4 3.8 1 5.4L9 13.3 4.2 15.9l1-5.4-4-3.8 5.4-.7z"/><use href="#st" x="22"/><use href="#st" x="44"/><use href="#st" x="66"/><use href="#st" x="88"/></g></svg></div>
  <p>Slate helps you see how many more days you need to work to reach your financial goal.</p>
  <div class="person"><div class="avatar" role="img" aria-label="Client portrait"></div><div><b>Renata</b><i>Founder of Northgate Corp</i></div></div>
</article>
<article class="testi" style="left:462px">
  <div class="stars"><svg width="110" height="18" viewBox="0 0 110 18"><g fill="#f2c200"><use href="#st"/><use href="#st" x="22"/><use href="#st" x="44"/><use href="#st" x="66"/><use href="#st" x="88"/></g></svg></div>
  <p>Slate helps you see how many more days you need to work to reach your financial goal.</p>
  <div class="person"><div class="avatar" role="img" aria-label="Client portrait" style="background:linear-gradient(135deg,#444,#111)"></div><div><b>Adrian</b><i>CEO</i></div></div>
</article>
<article class="testi" style="left:761px">
  <div class="stars"><svg width="110" height="18" viewBox="0 0 110 18"><g fill="#f2c200"><use href="#st"/><use href="#st" x="22"/><use href="#st" x="44"/><use href="#st" x="66"/><use href="#st" x="88"/></g></svg></div>
  <p>Slate helps you see how many more days you need to work to reach your financial goal.</p>
  <div class="person"><div class="avatar" role="img" aria-label="Client portrait" style="background:linear-gradient(135deg,#a9b6c9,#5c6474)"></div><div><b>Marcus</b><i>Business owner</i></div></div>
</article>

<!-- footer -->
<footer class="site-footer">
  <div class="foot-brand"><div class="foot-square"></div><span>Mireval Stone Development</span></div>
  <span class="foot-head" style="left:1001px;top:36px;font-size:14px">Get In Touch</span>
  <span class="social" style="left:1002px"></span>
  <span class="social" style="left:1036px"></span>
  <span class="social" style="left:1070px"></span>
  <div class="abs" style="left:97px;top:144px;width:1004px;height:2px;background:#6a6a6a"></div>

  <span class="foot-head" style="left:99px;top:188px">Pages</span>
  <span class="foot-link" style="left:99px;top:225px">Home</span>
  <span class="foot-link" style="left:99px;top:259px">About</span>
  <span class="foot-link" style="left:99px;top:292px">News</span>
  <span class="foot-link" style="left:99px;top:326px">Contact</span>

  <span class="foot-head" style="left:254px;top:188px">Legal</span>
  <span class="foot-link" style="left:254px;top:225px">Imprint</span>
  <span class="foot-link" style="left:254px;top:257px">Terms&amp; Condition</span>
  <span class="foot-link" style="left:254px;top:290px">Privacy</span>
  <span class="foot-link" style="left:254px;top:324px">Cookies</span>

  <span class="foot-head" style="left:409px;top:188px">Contact Info</span>
  <div class="info" style="top:226px"><svg width="16" height="12" viewBox="0 0 16 12"><rect x="1" y="1" width="14" height="10" fill="none" stroke="#ddd" stroke-width="1.4"/><path d="M1 1l7 6 7-6" stroke="#ddd" stroke-width="1.4" fill="none"/></svg>Info@MirevalStoneHomes.com</div>
  <div class="info" style="top:259px"><svg width="14" height="14" viewBox="0 0 24 24"><path d="M6 2l4 5-2 3a12 12 0 0 0 6 6l3-2 5 4-2 4C10 22 2 14 2 4z" fill="#ddd"/></svg>(555) 014-2290</div>
  <div class="info" style="top:292px"><svg width="14" height="16" viewBox="0 0 14 18"><path d="M7 17s6-6.5 6-10.5A6 6 0 0 0 1 6.5C1 10.5 7 17 7 17z" fill="#ddd"/><circle cx="7" cy="6.5" r="2.2" fill="#2e2e2f"/></svg><span>1480 Larkspur Ave<br>Suite 310<br>Fairhaven, CA. 90412</span></div>

  <span class="foot-head" style="left:729px;top:190px;font-size:12.5px">Stay Connected</span>
  <span class="foot-link" style="left:729px;top:222px;font-size:9px;color:#bbb">Get In Touch</span>
  <div class="abs body-text" style="left:729px;top:253px;width:252px;height:39px;background:#fff;font-size:13px;color:#777;padding:11px 16px">Enter Your Email</div>
  <div class="abs body-text" style="left:985px;top:253px;width:116px;height:39px;background:var(--red);font-size:13px;font-weight:600;display:flex;align-items:center;justify-content:center">Subscribe</div>

  <p class="center body-text" style="top:428px;font-size:12px;color:#aaa">© 2024 Mireval Stone Development All Rights Reserved.</p>
</footer>

</body>
</html>
```